Quellbyte Business cards template

We're looking for something modern and elegant. We are a reseller of technology (computers, datacenter, etc). Color theme would be "only" white with the incorporation of the blue that's present on our website (Quellbyte.com) and logo file. We would like for the card to provide all the necessary info for the specific person (Phone#, fax#, email, name, website URL) . I'm attaching the logo file to this request. Please have it show Lakeport/Fairhaven somewhere, without providing specific addresses.

Target Market(s)

All b2b

Industry/Entity Type

Business

Contact Information for Business Card

Please have the color scheme be represented by only the white and blue from our website (Quellbyte.com) and logo. We would like to logo on the card, but not big and overwhelming. This card will be used as a template for anybody within the company, it should display the user's name, phone#, fax#, email, job title and website URL. Please have it show Lakeport/Fairhaven somewhere, without providing our specific addresses. Really, we're looking for a clean, simple and elegant look.

Font styles to use
Serif

Requirements
Must have
• Please see card details
Nice to have
• Please see card details
Should not have
• Anything tacky or tagline.

```html
<!DOCTYPE html>
<html lang="en">
<head>
<meta charset="utf-8">
<title>Quellbyte Business Card</title>
<link rel="stylesheet" href="https://fonts.googleapis.com/css2?family=Roboto:wght@400;500;700&display=swap">
<style>
  :root {
    --page-bg: #e4e4e4;
    --brand-blue: #0b6fb5;
    --brand-blue-deep: #0a65a8;
    --card-white: #fbfbfb;
    --ink: #2f2f2f;
    --ink-blue: #1565a8;
  }
  html, body {
    margin: 0;
    padding: 0;
    overflow: hidden;
  }
  .canvas {
    position: relative;
    width: 1200px;
    height: 576px;
    background: var(--page-bg);
    font-family: "Roboto", Arial, sans-serif;
    overflow: hidden;
  }
  .card {
    position: absolute;
    top: 139px;
    height: 292px;
    border-radius: 13px;
    overflow: hidden;
    box-sizing: border-box;
  }
  .card--front {
    left: 82px;
    width: 484px;
    background: linear-gradient(180deg, var(--brand-blue) 0%, var(--brand-blue-deep) 100%);
  }
  .card--back {
    left: 602px;
    width: 480px;
    background: var(--card-white);
  }
  .wordmark {
    position: absolute;
    font-weight: 500;
    letter-spacing: 0.5px;
    line-height: 1;
    white-space: nowrap;
  }
  .card--front .wordmark {
    left: 50%;
    top: 122px;
    transform: translateX(-50%);
    font-size: 50px;
    color: #ffffff;
  }
  .card--back .wordmark {
    left: 250px;
    top: 212px;
    font-size: 40px;
    color: var(--brand-blue);
  }
  .edge-tab {
    position: absolute;
    left: -11px;
    top: 42px;
    width: 22px;
    height: 42px;
    border-radius: 50%;
    background: var(--brand-blue);
  }
  .person {
    position: absolute;
    left: 24px;
    top: 44px;
  }
  .person__name {
    margin: 0;
    font-size: 16.5px;
    font-weight: 700;
    color: var(--ink-blue);
    letter-spacing: 0.2px;
  }
  .person__title {
    margin: 4px 0 0;
    font-size: 11.5px;
    color: var(--ink);
  }
  .contact {
    position: absolute;
    left: 24px;
    top: 190px;
    margin: 0;
    padding: 0;
    list-style: none;
    font-size: 11.5px;
    color: var(--ink);
  }
  .contact__item {
    display: flex;
    align-items: center;
    height: 16.5px;
  }
  .contact__icon {
    width: 11px;
    height: 11px;
    margin: 0 12px 0 4px;
    fill: var(--ink-blue);
  }
  .cities {
    position: absolute;
    left: 24px;
    top: 243px;
    margin: 0;
    font-size: 12px;
    color: var(--ink);
  }
  .cities__divider {
    color: var(--brand-blue);
    margin: 0 5px;
  }
</style>
</head>
<body>
<main class="canvas">
  <section class="card card--front">
    <span class="wordmark">Quellbyte</span>
  </section>

  <section class="card card--back">
    <span class="edge-tab"></span>
    <div class="person">
      <p class="person__name">Daniel R. Ward</p>
      <p class="person__title">Managing Director</p>
    </div>

    <ul class="contact">
      <li class="contact__item">
        <svg class="contact__icon" viewBox="0 0 12 12" aria-hidden="true"><path d="M1 4.2C1 2.8 3 1.6 6 1.6s5 1.2 5 2.6v.9H8.4V4H3.6v1.1H1zM2.4 10.4l1.3-4.2h4.6l1.3 4.2zM6 9.2a1.2 1.2 0 1 0 0-2.4 1.2 1.2 0 0 0 0 2.4z"/></svg>
        +1 555-010-4821
      </li>
      <li class="contact__item">
        <svg class="contact__icon" viewBox="0 0 12 12" aria-hidden="true"><path fill-rule="evenodd" d="M6 .8a5.2 5.2 0 1 1 0 10.4A5.2 5.2 0 0 1 6 .8zm-.6 1.3C4.6 2.9 4.2 4.1 4.1 5.4h1.3zm1.2 0v3.3h1.3c-.1-1.3-.5-2.5-1.3-3.3zM2.1 5.4h1.2c.1-1.1.4-2.1.9-2.9a4 4 0 0 0-2.1 2.9zm7.8 0a4 4 0 0 0-2.1-2.9c.5.8.8 1.8.9 2.9zM2.1 6.6a4 4 0 0 0 2.1 2.9c-.5-.8-.8-1.8-.9-2.9zm2 0c.1 1.3.5 2.5 1.3 3.3V6.6zm2.5 0v3.3c.8-.8 1.2-2 1.3-3.3zm2.1 0c-.1 1.1-.4 2.1-.9 2.9a4 4 0 0 0 2.1-2.9z"/></svg>
        info@quellbyte.com
      </li>
      <li class="contact__item">
        <svg class="contact__icon" viewBox="0 0 12 12" aria-hidden="true"><path d="M.8 2.4h10.4v7.2H.8zm1.3 1.1v.4L6 6.6l3.9-2.7v-.4zm0 1.8v3.2h7.8V5.3L6 8z"/></svg>
        www.quellbyte.com
      </li>
    </ul>

    <p class="cities">Lakeport<span class="cities__divider">|</span>Fairhaven</p>

    <span class="wordmark">Quellbyte</span>
  </section>
</main>
</body>
</html>
```